Hospitality project presentation

I am developing a hospitality project and I need to present to the developer an outstanding presentation highlighting the overall look and feel. I will provide the text and most of the pictures (not all of them) some pictures (copyright free) will hae to be provided by the designer. Maximum number of pages 15, and zoom calls with me to make some adjustment if needed.

Industry/Entity Type

Hospitality

Font styles to use
Other font styles liked:
• calibri light

Requirements
Must have
• 15 slides
Nice to have
• Hospitality resort project look and feel

```html
<!DOCTYPE html>
<html lang="en">
<head>
<meta charset="utf-8">
<title>Luxury Private Retreat – Presentation Spread</title>
<link href="https://fonts.googleapis.com/css2?family=Hanken+Grotesk:wght@300;400;500;600;700&display=swap" rel="stylesheet">
<style>
  :root {
    --board: #4a4a4a;
    --paper: #ffffff;
    --mist: #f3f4f4;
    --ink: #1a1a1a;
    --night: #161616;
    --gold: #d4b032;
    --muted: #555555;
  }
  * { box-sizing: border-box; margin: 0; padding: 0; }
  html, body { width: 1200px; height: 744px; overflow: hidden; background: var(--board); }
  body { position: relative; font-family: "Hanken Grotesk", Arial, sans-serif; color: var(--ink); }

  .slide { position: absolute; overflow: hidden; }

  /* Cover */
  .cover { left: 0; top: 0; width: 900px; height: 507px; background: var(--paper); }
  .cover-photo {
    position: absolute; left: 0; top: 36px; width: 900px; height: 300px;
    background: linear-gradient(180deg, #ffffff 0%, #ffffff 20%, #5b5e63 30%, #4d5055 44%, #e4ddd0 54%, #ddd6c8 76%, #7d9a4e 88%, #8aa35c 100%);
  }
  .cover-band { position: absolute; left: 0; top: 336px; width: 900px; height: 80px; background: linear-gradient(180deg, #d6d5d0, var(--mist)); }
  .cover-rule { position: absolute; left: 42px; top: 373px; width: 810px; height: 2px; background: var(--gold); }
  .cover-title { position: absolute; left: 43px; top: 382px; font-size: 23px; font-weight: 500; letter-spacing: 4.2px; }
  .cover-place { position: absolute; left: 43px; top: 413px; font-size: 12px; letter-spacing: 1.2px; color: var(--gold); }
  .cover-season { position: absolute; right: 49px; top: 381px; font-size: 13.5px; letter-spacing: 1.3px; }

  .brand { position: absolute; display: flex; flex-direction: column; }
  .brand-name { display: flex; align-items: center; gap: 6px; font-weight: 600; color: var(--ink); letter-spacing: .5px; }
  .brand-name::before { content: ""; width: 9px; height: 9px; background: var(--gold); }
  .brand-sub { font-size: 7.5px; letter-spacing: 2.4px; color: var(--muted); margin-top: 2px; margin-left: 15px; }
  .cover .brand { left: 698px; top: 44px; }
  .cover .brand-name { font-size: 21px; }

  /* Intro slide */
  .intro { left: 928px; top: 0; width: 272px; height: 507px;
    background: linear-gradient(160deg, #d8d9d8 0%, #eeeeec 40%, #e6e6e4 100%); }
  .intro-panel { position: absolute; left: 0; top: 79px; width: 272px; height: 428px; background: rgba(255,255,255,.82); }
  .intro-rule { position: absolute; left: 66px; top: 163px; width: 206px; height: 2px; background: var(--gold); }
  .intro-heading { position: absolute; left: 65px; top: 172px; font-size: 22.5px; font-weight: 300; line-height: 28px; }
  .intro-heading strong { color: var(--gold); font-weight: 600; }
  .intro-body { position: absolute; left: 65px; top: 274px; width: 198px; font-size: 8.8px; line-height: 12.3px; }
  .intro-body p { margin-bottom: 9px; }
  .intro .brand { left: 64px; top: 452px; }
  .intro .brand-name { font-size: 15px; }
  .intro .brand-sub { font-size: 6px; }

  /* Opportunity slide */
  .opportunity { left: 0; top: 535px; width: 900px; height: 209px; background: var(--night); }
  .opportunity-photo { position: absolute; left: 519px; top: 0; width: 381px; height: 209px;
    background: linear-gradient(180deg, #e9e9ea 0%, #dcdad7 55%, #c8c4bc 100%); }
  .opportunity-rule { position: absolute; left: 55px; top: 96px; width: 807px; height: 2px; background: var(--gold); }
  .opportunity-tag { position: absolute; left: 698px; top: 62px; width: 163px; height: 35px; background: var(--gold);
    color: #fff; font-size: 22px; font-weight: 400; display: flex; align-items: center; justify-content: center; }
  .opportunity-heading { position: absolute; left: 56px; top: 138px; font-size: 22px; line-height: 28px; color: #fff; font-weight: 400; }
  .opportunity-heading strong { color: var(--gold); font-weight: 600; display: block; }
  .feature { position: absolute; left: 275px; top: 144px; display: flex; gap: 9px; }
  .feature-icon { width: 24px; height: 28px; flex: none; }
  .feature-title { color: #fff; font-size: 10.5px; font-weight: 600; margin-bottom: 5px; }
  .feature-text { color: #fff; font-size: 7.8px; line-height: 11.6px; width: 170px; }

  /* Detail slide */
  .detail { left: 928px; top: 535px; width: 272px; height: 209px;
    background: linear-gradient(135deg, #cfcbc6 0%, #ebe8e4 45%, #e2dfda 100%); }
</style>
</head>
<body>

<section class="slide cover">
  <div class="cover-photo" role="img" aria-label="Photograph of a stone luxury villa with a dark hipped roof and landscaped lawn"></div>
  <div class="cover-band" role="img" aria-label="Faded driveway in front of the villa"></div>
  <div class="brand">
    <span class="brand-name">HAVENLEA</span>
    <span class="brand-sub">RESIDENCES</span>
  </div>
  <div class="cover-rule"></div>
  <h1 class="cover-title">LUXURY PRIVATE RETREAT</h1>
  <p class="cover-place">TUSCANY, FRANCE</p>
  <p class="cover-season">SUMMER 2022</p>
</section>

<section class="slide intro">
  <div class="intro-panel"></div>
  <div class="intro-rule"></div>
  <h2 class="intro-heading">Blending <strong>premium<br>hospitality</strong> with<br>suburban chic</h2>
  <div class="intro-body">
    <p>Lorem ipsum dolor sit amet, consectetur adipiscing elit. Mauris ipsum odio, vehicula ac venenatis at, maximus in dolor. Vivamus euismod venenatis aliquam.</p>
    <p>Maecenas posuere consequat lectus sed faucibus. Sed dignissim nunc vitae fringilla malesuada. Sed ac maximus diam. Nulla pulvinar purus at aliquet tincidunt.</p>
    <p>Duis iaculis feugiat nibh in pulvinar. Aenean eget nibh sit amet tellus.</p>
  </div>
  <div class="brand">
    <span class="brand-name">HAVENLEA</span>
    <span class="brand-sub">RESIDENCES</span>
  </div>
</section>

<section class="slide opportunity">
  <div class="opportunity-photo" role="img" aria-label="Photograph of a bright interior with ceiling fan and framed artwork"></div>
  <div class="opportunity-rule"></div>
  <div class="opportunity-tag">Opportunity</div>
  <h2 class="opportunity-heading">Lorem ipsum<strong>dolor sit amet</strong></h2>
  <div class="feature">
    <svg class="feature-icon" viewBox="0 0 24 28" fill="var(--gold)">
      <polygon points="12,1 5,10 9,10 3,17 8,17 1,24 23,24 16,17 21,17 15,10 19,10"/>
      <rect x="10" y="24" width="4" height="4"/>
    </svg>
    <div>
      <h3 class="feature-title">Sed luctus luctus posuere.</h3>
      <p class="feature-text">Pellentesque habitant morbi tristique senectus et netus et malesuada fames ac turpis egestas. Sed eu lacinia mauris. Proin nisi odio, pellentesque quis nulla eget,</p>
    </div>
  </div>
</section>

<section class="slide detail" role="img" aria-label="Photograph of a bathroom corner with mirror and abstract gold artwork"></section>

</body>
</html>
```